Minimalist Professional Business Card Design

We will be revamping our marketing materials: Business cards, Website and Catalogs.
Our Overall Design direction is to have a Minimalist artwork with Professionalism and Premium feel. The revamp starts with the new business card design followed by the others. Thus the designer whom work is selected for this job will likely to follow through with the subsequent jobs.

Target Market(s)

Upscale

Industry/Entity Type

Manufacturing

Contact Information for Business Card

For the Business Cards, the following are required:
. Minimalist yet Professional and Premium Feel
. Background Colors: white and / or light pastel yellow and if needed to smoothen the yellow, the light grey can be incorporated. We are changing our corporate bright yellow to either one of the three alternatives:
1. Soylant yellow CMYK (1%, 0%, 52%, 3%)
2. Popcorn yellow CMYK (0%, 0%, 33%, 0%)
3. Papaya yellow CMYK (0%, 0%, 51%, 0%)

Information to be inputed in the business cards:

Name: Barlen Moritova
Position: Managing Director

Company's name: Vellomar Valves Pte. Ltd.
Address: 512 Halvick Lane #07-09B
Singapore 617302
Tel: (65) 6281 4096
Fax: (65) 6294 7118
Email: barlen@vellomarvalves-example.com
Website: www.vellomarvalves-example.com
Skype: Vellomar.Valves
Whatsapp/ Line/ Viber/ WeChat: (65) 9372 6081

Company's Logo
Company's Slogan
Two product photos placed side by side (if this gets into the way of the design, it is OK not to include them)

Font styles to use
Serif

Colors
ffffff

Requirements
Must have
• Minimalist
Should not have
• Messy, crowded, playful

```html
<!DOCTYPE html>
<html lang="en">
<head>
<meta charset="utf-8">
<title>Vellomar Valves – Business Card</title>
<link href="https://fonts.googleapis.com/css2?family=Open+Sans:wght@400;600;700&display=swap" rel="stylesheet">
<style>
  :root {
    --backdrop: #e6e4e0;
    --card-white: #fbfbfa;
    --card-yellow: #fdfbc6;
    --ink: #4a4a4a;
    --ink-soft: #6b6b6b;
    --rule: #cfcfcf;
    --brand: #555555;
    --steel-light: #eef0f2;
    --steel-dark: #a9afb5;
  }
  * { box-sizing: border-box; margin: 0; padding: 0; }
  html, body {
    width: 1200px; height: 844px; overflow: hidden;
    background: var(--backdrop);
    font-family: "Open Sans", Arial, sans-serif;
    color: var(--ink);
  }
  .stage {
    position: relative; width: 1200px; height: 844px;
    display: flex; align-items: center; justify-content: center; gap: 40px;
  }
  .card {
    position: relative; width: 540px; height: 310px;
    box-shadow: 0 6px 18px rgba(0,0,0,.18);
  }
  .card--front { background: var(--card-white); }
  .card--back { background: var(--card-yellow); }

  /* brand lockup */
  .brand { display: flex; flex-direction: column; align-items: center; color: var(--brand); }
  .brand__dot { border: 6px solid var(--brand); border-radius: 50%; }
  .brand__name { font-weight: 700; letter-spacing: 1px; text-transform: uppercase; line-height: 1; }

  .card--front .brand { position: absolute; top: 22px; right: 34px; }
  .card--front .brand__dot { width: 52px; height: 52px; border-width: 5px; margin-bottom: 6px; }
  .card--front .brand__name { font-size: 22px; }

  .rule { position: absolute; left: 30px; right: 30px; height: 1px; background: var(--rule); }
  .rule--1 { top: 112px; }
  .rule--2 { top: 132px; }

  .details { position: absolute; left: 30px; top: 150px; font-size: 12.5px; line-height: 1.35; }
  .details__name { font-size: 16px; font-weight: 700; text-transform: uppercase; letter-spacing: .3px; }
  .details__role { color: var(--ink-soft); margin-bottom: 8px; }
  .details__line b { font-weight: 700; }
  .details__messaging { display: flex; align-items: center; gap: 14px; margin-top: 8px; }
  .details__mobile { display: flex; align-items: center; gap: 6px; font-size: 14px; }
  .details__handle { display: flex; align-items: center; gap: 5px; }
  .marker { width: 11px; height: 11px; border: 1.5px solid var(--ink); border-radius: 50%; display: inline-block; }
  .details__address { margin-top: 10px; font-size: 13px; }

  .card--back .brand { position: absolute; left: 50%; top: 72px; transform: translateX(-50%); }
  .card--back .brand__dot { width: 84px; height: 84px; border-width: 8px; margin-bottom: 12px; }
  .card--back .brand__name { font-size: 34px; letter-spacing: 2px; }
  .slogan {
    position: absolute; left: 0; right: 0; top: 228px; text-align: center;
    font-size: 12px; font-weight: 700; letter-spacing: .6px; text-transform: uppercase; color: var(--brand);
  }
  .product {
    position: absolute; width: 34px; border-radius: 6px;
    background: linear-gradient(90deg, var(--steel-dark), var(--steel-light) 45%, var(--steel-dark));
  }
  .product--left { left: 60px; top: 96px; height: 130px; }
  .product--right { right: 60px; top: 40px; height: 150px; }
</style>
</head>
<body>
<main class="stage">
  <section class="card card--front">
    <div class="brand">
      <span class="brand__dot"></span>
      <span class="brand__name">Vellomar</span>
    </div>
    <div class="rule rule--1"></div>
    <div class="rule rule--2"></div>
    <div class="details">
      <p class="details__name">Barlen Moritova</p>
      <p class="details__role">Managing Director</p>
      <p class="details__line"><b>P:</b> (65) 6281 4096 | <b>F:</b> (65) 6294 7118</p>
      <p class="details__line"><b>E:</b> barlen@vellomarvalves-example.com | www.vellomarvalves-example.com</p>
      <div class="details__messaging">
        <span class="details__mobile"><span class="marker"></span>(65) 9372 6081</span>
        <span class="details__handle"><span class="marker"></span>Vellomar.Valves</span>
      </div>
      <p class="details__address">Vellomar Valves Pte. Ltd.<br>512 Halvick Lane #07-09B Singapore 617302</p>
    </div>
  </section>

  <section class="card card--back">
    <div class="product product--left" role="img" aria-label="Product photo: stainless steel valve unit"></div>
    <div class="brand">
      <span class="brand__dot"></span>
      <span class="brand__name">Vellomar</span>
    </div>
    <p class="slogan">Made with pride | For heavy duty</p>
    <div class="product product--right" role="img" aria-label="Product photo: stainless steel valve body"></div>
  </section>
</main>
</body>
</html>
```